Restaurant Finder Website Design

I need to create a website that will help people find restaurants around a zip code or address.

I would like to have a very clean and simple design. I will need a design for the homepage, that should be very clean and simple to use. its where the users will launch their search. I am thinking something like tavlex like.. big search field with a very clean page where users can create an account or restaurants subscribe to the service.

Also need the design of the search results page, I would like to display a big map with the results and a list on the side or the bottom of the map.

Also need a profile page for the users that sign up to the site.

Mostly what I need are guidelines and color coordinated elements, like a general layout and buttons that work together. I would like to know what the action buttons and elements should look like. Because its going to have some more detail pages.

Target Market(s)

People in general, mainly people that work at an office and have to find a place for lunch every day.

Industry/Entity Type

Restaurant

Number of Pages Required

4 page

Font styles to use
Serif
Sans Serif

Requirements
Must have
• It must be a really simple and clean design but look edgy.

```html
<!DOCTYPE html>
<html lang="en">
<head>
<meta charset="utf-8">
<title>Dinevia – Sign up</title>
<link href="https://fonts.googleapis.com/css2?family=Montserrat:wght@400;500;600;700&family=Gabriela&display=swap" rel="stylesheet">
<style>
  :root {
    --red: #c62027;
    --ink: #2b2b2b;
    --muted: #9a9a9a;
    --line: #c4c4c4;
    --white: #ffffff;
  }
  * { box-sizing: border-box; margin: 0; padding: 0; }
  html, body { width: 954px; height: 1200px; overflow: hidden; }
  body { position: relative; background: var(--white); font-family: "Montserrat", sans-serif; color: var(--ink); }

  .site-header {
    position: absolute; left: 0; top: 0; width: 954px; height: 82px;
    box-shadow: 0 2px 4px rgba(0,0,0,0.15); background: var(--white);
  }
  .brand { position: absolute; display: flex; align-items: center; gap: 8px; font-size: 15px; font-weight: 600; }
  .brand-dot { width: 26px; height: 26px; border-radius: 50%; border: 2px solid var(--red); }
  .site-header .brand { left: 128px; top: 28px; color: var(--ink); }
  .main-nav { position: absolute; top: 30px; left: 483px; height: 24px; display: flex; align-items: center; }
  .main-nav a { color: var(--ink); text-decoration: none; font-size: 11px; font-weight: 600; position: absolute; white-space: nowrap; }
  .nav-cta {
    border: 1.5px solid var(--red); border-radius: 13px; color: var(--red) !important;
    width: 95px; height: 24px; display: flex; align-items: center; justify-content: center;
  }

  .page-title {
    position: absolute; top: 136px; width: 954px; text-align: center;
    font-family: "Gabriela", serif; font-weight: 400; font-size: 24px; color: var(--ink);
  }

  .role { position: absolute; top: 226px; width: 90px; text-align: center; font-family: "Gabriela", serif; font-size: 14px; }
  .role svg { display: block; margin: 0 auto 10px; }
  .role-customer { left: 371px; color: var(--muted); }
  .role-provider { left: 492px; color: var(--ink); }

  .field {
    position: absolute; height: 43px; border: 1px solid var(--line);
    display: flex; align-items: center; padding-left: 23px;
    font-size: 10.5px; font-weight: 500; color: var(--muted); background: var(--white);
  }
  .field-full { left: 307px; width: 340px; }
  .field-left { left: 307px; width: 161px; }
  .field-right { left: 486px; width: 161px; }
  .field-active { border-color: var(--red); }
  .field-select svg { position: absolute; right: 12px; top: 14px; }

  .submit {
    position: absolute; left: 307px; top: 807px; width: 340px; height: 43px;
    background: var(--red); color: var(--white); border: none;
    font-family: "Montserrat", sans-serif; font-size: 11px; font-weight: 600;
  }

  .site-footer { position: absolute; left: 0; top: 948px; width: 954px; height: 252px; background: var(--red); color: var(--white); }
  .site-footer .brand { left: 408px; top: 33px; color: var(--white); }
  .site-footer .brand-dot { border-color: var(--white); }
  .footer-nav { position: absolute; top: 99px; width: 954px; display: flex; justify-content: center; gap: 22px; }
  .footer-nav a { color: var(--white); text-decoration: none; font-size: 10.5px; font-weight: 600; }
  .social { position: absolute; top: 145px; left: 356px; display: flex; gap: 22px; }
  .social span { width: 30px; height: 30px; border-radius: 50%; background: var(--white); display: block; }
  .copyright { position: absolute; top: 207px; width: 954px; text-align: center; font-family: "Gabriela", serif; font-size: 11px; }
</style>
</head>
<body>
  <header class="site-header">
    <div class="brand"><span class="brand-dot"></span>Dinevia</div>
    <nav class="main-nav">
      <a href="#" style="left:0">Home</a>
      <a href="#" style="left:60px">Explore</a>
      <a href="#" style="left:131px">Pricing</a>
      <a href="#" style="left:198px">Blog</a>
      <a href="#" class="nav-cta" style="left:247px;top:0">Sign up</a>
    </nav>
  </header>

  <h1 class="page-title">Sign up</h1>

  <div class="role role-customer">
    <svg width="36" height="36" viewBox="0 0 36 36" fill="none" stroke="#9a9a9a" stroke-width="1.4">
      <circle cx="18" cy="18" r="16.5"/>
      <circle cx="18" cy="14" r="6"/>
      <path d="M8 30c2-6 6-8 10-8s8 2 10 8"/>
    </svg>
    Customer
  </div>
  <div class="role role-provider">
    <svg width="36" height="36" viewBox="0 0 36 36" fill="none" stroke="#c62027" stroke-width="1.4" stroke-linecap="round">
      <ellipse cx="9" cy="8" rx="4" ry="6" transform="rotate(-45 9 8)"/>
      <path d="M12 12L31 31"/>
      <path d="M29 3L7 30"/>
      <path d="M25 2l-3 6M29 5l-4 5M32 9l-6 3"/>
    </svg>
    Provider
  </div>

  <form>
    <div class="field field-full field-active" style="top:326px">Company Name</div>
    <div class="field field-left" style="top:386px">First Name</div>
    <div class="field field-right" style="top:386px">Last Name</div>
    <div class="field field-left" style="top:446px">Username</div>
    <div class="field field-right" style="top:446px">Email</div>
    <div class="field field-left" style="top:506px">Password</div>
    <div class="field field-right" style="top:506px">Confirm Password</div>
    <div class="field field-full" style="top:566px">Address</div>
    <div class="field field-left" style="top:626px">State</div>
    <div class="field field-right" style="top:626px">Zipcode</div>
    <div class="field field-left" style="top:686px">Country</div>
    <div class="field field-right field-select" style="top:686px">Category
      <svg width="16" height="16" viewBox="0 0 16 16" fill="none" stroke="#9a9a9a" stroke-width="1"><circle cx="8" cy="8" r="7.3"/><path d="M8 4v7M5.5 8.5L8 11l2.5-2.5"/></svg>
    </div>
    <div class="field field-left field-select" style="top:746px">Select Package
      <svg width="16" height="16" viewBox="0 0 16 16" fill="none" stroke="#9a9a9a" stroke-width="1"><circle cx="8" cy="8" r="7.3"/><path d="M8 4v7M5.5 8.5L8 11l2.5-2.5"/></svg>
    </div>
    <button type="button" class="submit">Sign up</button>
  </form>

  <footer class="site-footer">
    <div class="brand"><span class="brand-dot"></span>Dinevia</div>
    <nav class="footer-nav">
      <a href="#">Home</a><a href="#">Explore</a><a href="#">Pricing</a><a href="#">Blog</a><a href="#">Sign Up</a>
    </nav>
    <div class="social" aria-label="Social links">
      <span></span><span></span><span></span><span></span><span></span>
    </div>
    <p class="copyright">© 2016 Pizza Restaurant</p>
  </footer>
</body>
</html>
```